Ridgeway Pest Solutions *

I work as a pest control technician with other company. Now I want to start my own business.

So I want a new logo and business card design (both side of the card).

Colour combination I like Green/Red/white.

On card may have some sort of insect/ but not sure.

Target Market(s)

Anyone in Sydney. There is no specific target.

Industry/Entity Type

Business

Logo Text

Ridgeway Pest Solutions

```html
<!DOCTYPE html>
<html lang="en">
<head>
<meta charset="UTF-8">
<title>Ridgeway Pest Solutions — Business Card</title>
<link href="https://fonts.googleapis.com/css2?family=Poppins:wght@400;500;700;800&display=swap" rel="stylesheet">
<style>
  :root {
    --red: #ea2227;
    --green: #1f8a3a;
    --green-light: #5cb13f;
    --ink: #141414;
    --white: #ffffff;
    --backdrop: #3a3a3c;
    --ghost: #e9ece8;
  }
  * { margin: 0; padding: 0; box-sizing: border-box; }
  html, body { width: 1200px; height: 900px; overflow: hidden; }
  body {
    background: var(--backdrop);
    font-family: "Poppins", sans-serif;
    position: relative;
  }
  .card {
    position: absolute;
    width: 620px;
    height: 354px;
    border-radius: 22px;
    overflow: hidden;
    box-shadow: 0 10px 24px rgba(0,0,0,.35);
  }

  /* Back side */
  .card-back {
    left: 470px; top: 50px;
    background: var(--red);
    color: var(--white);
  }
  .card-back .brand {
    position: absolute;
    left: 0; right: 0; top: 120px;
    display: flex; align-items: center; justify-content: center; gap: 16px;
  }
  .card-back .brand-dot {
    width: 62px; height: 62px; border-radius: 50%;
    background: var(--white);
  }
  .card-back .brand-name {
    font-weight: 800; font-size: 34px; line-height: 1.05;
    text-transform: uppercase; letter-spacing: .5px;
  }
  .card-back .licence {
    position: absolute; left: 0; right: 0; top: 262px;
    text-align: center; font-size: 15px; letter-spacing: 1px;
    text-transform: uppercase;
  }

  /* Front side */
  .card-front {
    left: 110px; top: 480px;
    background: var(--white);
    color: var(--ink);
  }
  .card-front .ghost-ring {
    position: absolute; right: 40px; top: 120px;
    width: 190px; height: 190px; border-radius: 50%;
    background: var(--ghost);
  }
  .card-front .brand {
    position: absolute; left: 34px; top: 30px;
    display: flex; align-items: center; gap: 16px;
  }
  .card-front .brand-dot {
    width: 70px; height: 70px; border-radius: 50%;
    background: var(--red);
  }
  .card-front .brand-name {
    font-weight: 800; font-size: 34px; line-height: 1.05;
    text-transform: uppercase; color: var(--ink);
  }
  .card-front .person {
    position: absolute; left: 34px; top: 130px;
  }
  .person-name {
    font-weight: 700; font-size: 17px; text-transform: uppercase; letter-spacing: .3px;
  }
  .person-role {
    font-size: 14px; color: var(--red); text-transform: uppercase; letter-spacing: .3px;
  }
  .card-front .divider {
    position: absolute; left: 34px; right: 34px; top: 186px;
    height: 1px; background: var(--ink);
  }
  .contact {
    position: absolute; left: 34px; top: 200px;
    list-style: none; font-size: 15px;
  }
  .contact li { display: flex; align-items: center; gap: 10px; margin-bottom: 6px; }
  .contact svg { width: 16px; height: 16px; flex: none; }
  .stripe { position: absolute; height: 6px; }
  .stripe-red { left: 0; width: 260px; top: 300px; background: var(--red); }
  .stripe-green { left: 260px; width: 250px; top: 300px; background: var(--green); }
  .stripe-tail { right: 0; width: 40px; top: 300px; background: var(--green); }
  .eco-badge {
    position: absolute; left: 520px; top: 264px;
    width: 62px; height: 62px; border-radius: 50%;
    background: radial-gradient(circle at 40% 35%, var(--green-light), var(--green));
  }
</style>
</head>
<body>

  <section class="card card-back" aria-label="Business card back">
    <div class="brand">
      <span class="brand-dot"></span>
      <span class="brand-name">Ridgeway<br>Pest Solutions</span>
    </div>
    <p class="licence">Licence No: 4072913</p>
  </section>

  <section class="card card-front" aria-label="Business card front">
    <div class="ghost-ring"></div>
    <div class="brand">
      <span class="brand-dot"></span>
      <span class="brand-name">Ridgeway<br>Pest Solutions</span>
    </div>
    <div class="person">
      <p class="person-name">Tarek Rahman (Tari)</p>
      <p class="person-role">Pest Control Technician</p>
    </div>
    <div class="divider"></div>
    <ul class="contact">
      <li>
        <svg viewBox="0 0 16 16"><circle cx="8" cy="8" r="8" fill="#ea2227"/><path d="M5 4.5c.5-.5 1-.4 1.3 0l.8 1.2c.2.4.1.8-.2 1l-.4.3c.4.9 1.1 1.6 2 2l.3-.4c.3-.3.7-.4 1-.2l1.2.8c.4.3.5.8 0 1.3-.6.6-1.5.8-2.4.4-1.7-.7-3-2-3.7-3.7-.4-.9-.2-1.8.1-2.7z" fill="#fff"/></svg>
        555-210-4830
      </li>
      <li>
        <svg viewBox="0 0 16 16"><circle cx="8" cy="8" r="8" fill="#ea2227"/><rect x="4" y="5.2" width="8" height="5.6" rx=".6" fill="none" stroke="#fff" stroke-width="1"/><path d="M4.2 5.6 8 8.4l3.8-2.8" fill="none" stroke="#fff" stroke-width="1"/></svg>
        info@ridgewaypest.com
      </li>
    </ul>
    <div class="stripe stripe-red"></div>
    <div class="stripe stripe-green"></div>
    <div class="stripe stripe-tail"></div>
    <div class="eco-badge" role="img" aria-label="Eco-friendly badge"></div>
  </section>

</body>
</html>
```